BrightLedger, The Ultimate Franchise Online Training Platform

Need Roll-up Banner Design measuring 30 x 80 inches, Looking for a design that is clean, professional, not cliche. We’re open to shape motifs like a circle, square, or swoosh—choose what best reinforces motion, strength, or innovation. Consistency is key: this should look great whether it's on a banner, a slide deck, or our letterhead. Our business is serving as a Franchisee e-learning platform providing vetted information from experts, an online library and masterclasses. Uploaded examples of Banner art with correct wording. Wording can be:
THE ULTIMATE FRANCHISEE TOOLKIT
Your 24/7 Edge for Franchise Success
On-Demand Resource Library
Monthly Masterclasses
Direct Access to Industry Experts
“Your Entrepreneurial Edge.”
OR
“Opening your first or your fifth, BrightLedger is your unfair advantage.”
Catapult your learning curve.
Avoid costly mistakes.
Grow with a community that gets it.
Join the Movement. Unlock Your Toolkit Today.
Updates

My apologies to designers I haven´t voted or provided updates for yet. We are still reviewing designs as the last call will be made by the owners and we live in different time zones. Thank you!

Target Market(s)

Business Owners, from small to mid

Industry/Entity Type

Small Business Owners, Franchisees

Font styles to use
Other font styles liked:
• Poppins, Roboto, Garamond, Montserrat, Lato

Colors

Designer to choose colors to be used in the design.

Requirements
Must have
• Consistency in color guide, font and wording
Nice to have
• Open to pretty much fluid designs, simple and uncluttered

```html
<!DOCTYPE html>
<html lang="en">
<head>
<meta charset="utf-8">
<title>BrightLedger Roll-up Banner</title>
<link rel="stylesheet" href="https://fonts.googleapis.com/css2?family=Montserrat:wght@400;500;700;800;900&display=swap">
<style>
  :root {
    --ink: #262b1e;
    --lime: #a6cc3f;
    --paper: #ffffff;
    --stage: #161616;
  }
  * { margin: 0; padding: 0; box-sizing: border-box; }
  html, body { width: 1200px; height: 1200px; overflow: hidden; background: var(--stage); }
  body { font-family: "Montserrat", sans-serif; color: var(--ink); }

  .banner {
    position: absolute; left: 390px; top: 40px;
    width: 420px; height: 1120px;
    background: var(--paper); overflow: hidden;
  }
  .line {
    position: absolute; left: 0; width: 100%;
    text-align: center; white-space: nowrap; line-height: 1;
  }

  .headline-opening { top: 76px; font-size: 64px; font-weight: 900; letter-spacing: 0.5px; }
  .headline-first { top: 132px; font-size: 44px; font-weight: 400; color: var(--lime); }
  .headline-fifth { top: 188px; font-size: 42px; font-weight: 400; }
  .headline-first b, .headline-fifth b { font-weight: 800; }
  .small-caps { font-size: 28px; }

  .brand { position: absolute; top: 268px; left: 0; width: 100%; text-align: center; }
  .brand-square { width: 210px; height: 210px; margin: 0 auto; background: var(--lime); }
  .brand-name { margin-top: 24px; font-size: 34px; line-height: 1; font-weight: 500; letter-spacing: 3px; color: var(--ink); }

  .claim { top: 612px; font-size: 40px; font-weight: 400; line-height: 51px; }

  .benefit { font-size: 17.5px; font-weight: 400; }
  .benefit-1 { top: 734px; }
  .benefit-2 { top: 775px; }
  .benefit-3 { top: 818px; }
  .rule { position: absolute; left: 55px; width: 310px; height: 2px; background: var(--lime); }
  .rule-1 { top: 760px; }
  .rule-2 { top: 802px; }

  .cta {
    position: absolute; left: 0; top: 860px; width: 100%; height: 146px;
    background: var(--lime); border-bottom: 8px solid var(--ink);
    text-align: center; padding-top: 12px;
  }
  .cta p { font-size: 30px; font-weight: 800; line-height: 39px; letter-spacing: 0.3px; }
  .cta-tail { position: absolute; left: 250px; top: 998px; }

  .web { top: 1054px; font-size: 27px; font-weight: 800; }
  .web span { color: var(--lime); }
</style>
</head>
<body>
  <main class="banner">
    <h1 class="line headline-opening">OPENING</h1>
    <p class="line headline-first">YOUR <b>FIRST</b></p>
    <p class="line headline-fifth"><span class="small-caps">OR</span> YOUR <b>FIFTH,</b></p>

    <div class="brand">
      <div class="brand-square"></div>
      <p class="brand-name">BRIGHTLEDGER</p>
    </div>

    <p class="line claim">IS YOUR UNFAIR<br>ADVANTAGE.</p>

    <p class="line benefit benefit-1">CATAPULT YOUR LEARNING CURVE.</p>
    <div class="rule rule-1"></div>
    <p class="line benefit benefit-2">AVOID COSTLY MISTAKES.</p>
    <div class="rule rule-2"></div>
    <p class="line benefit benefit-3">GROW WITH A COMMUNITY THAT GETS IT.</p>

    <section class="cta">
      <p>JOIN THE MOVEMENT<br>UNLOCK YOUR<br>TOOLKIT TODAY</p>
    </section>
    <svg class="cta-tail" width="120" height="46" viewBox="0 0 120 46" aria-hidden="true">
      <polygon points="0,0 120,0 4,46" fill="var(--ink)"/>
      <polygon points="10,0 95,0 12,32" fill="var(--lime)"/>
    </svg>

    <p class="line web">www.<span>BRIGHTLEDGER</span>.com</p>
  </main>
</body>
</html>
```